Business Card for a Jewellery Brand

Business card for an upscale jewellery brand. Attached is the brand logo and icon and color board. I am looking for two card versions: one for the founder and one is generic. The card should be elegant and convey upscale and premium feel. I am open to both square and rectangle card shapes.

Industry/Entity Type

Jewelry

Contact Information for Business Card

Two cards: (1) Suneha Parmeshwar (Founder) (2) General
(1) Suneha Parmeshwar card should have Name: Suneha Parmeshwar, Title: Founder Email id: suneha@quelm.com.au. Phone no: +61452190437
(2) Generic card should have Email id: info@quelm.com.au. Phone no: +61431267508

Requirements
Must have
• Workmark
• ICON
• Phone no
• Email ID
• ABN: 48291175034 (Note: ABN is Business number in Australia)
• Website: www.quelm.com.au
• Instagram: quelm_jewellery
• Facebook: @quelmjewellery
Nice to have
• Tagline

```html
<!DOCTYPE html>
<html lang="en">
<head>
<meta charset="utf-8">
<title>QUELM Business Cards</title>
<link rel="stylesheet" href="https://fonts.googleapis.com/css2?family=Lato:wght@300;400;700&display=swap">
<style>
  :root {
    --rose: #e5948f;
    --rose-deep: #df8a86;
    --paper: #ffffff;
    --backdrop: #e9e6e4;
    --text-rose: #e08c88;
  }
  * { margin: 0; padding: 0; box-sizing: border-box; }
  html, body { width: 1200px; height: 880px; overflow: hidden; }
  body {
    background: var(--backdrop);
    font-family: "Lato", sans-serif;
    position: relative;
  }
  .card {
    position: absolute;
    left: 260px;
    width: 680px;
    height: 390px;
    border-radius: 26px;
    box-shadow: 0 8px 24px rgba(0,0,0,0.12);
    overflow: hidden;
  }
  .card-front { top: 32px; background: var(--rose); }
  .card-back { top: 458px; background: var(--paper); color: var(--text-rose); }

  /* front */
  .front-brand {
    position: absolute; left: 0; right: 0; top: 120px;
    display: flex; flex-direction: column; align-items: center; gap: 18px;
  }
  .brand-dot {
    width: 64px; height: 64px; border-radius: 50%;
    border: 3px solid var(--paper);
  }
  .front-wordmark {
    color: var(--paper); font-weight: 300; font-size: 40px; letter-spacing: 14px;
    padding-left: 14px;
  }
  .front-web {
    position: absolute; left: 0; right: 0; top: 300px; text-align: center;
    color: var(--paper); font-size: 17px; letter-spacing: 2px;
  }

  /* back */
  .back-brand {
    position: absolute; right: 52px; top: 44px;
    display: flex; flex-direction: column; align-items: center; gap: 14px;
  }
  .back-brand .brand-dot { width: 52px; height: 52px; border-color: var(--text-rose); }
  .back-wordmark {
    color: var(--text-rose); font-weight: 300; font-size: 44px; letter-spacing: 16px;
    padding-left: 16px;
  }
  .rule {
    position: absolute; left: 40px; right: 40px; top: 236px;
    height: 2px; background: var(--text-rose);
  }
  .person { position: absolute; left: 40px; top: 172px; }
  .person-name { font-weight: 700; font-size: 24px; }
  .person-role { font-size: 16px; margin-top: 2px; }
  .contact-list, .social-list {
    position: absolute; top: 262px; list-style: none;
    font-size: 16px; display: flex; flex-direction: column; gap: 10px;
  }
  .contact-list { left: 40px; }
  .social-list { left: 290px; }
  .contact-list li, .social-list li { display: flex; align-items: center; gap: 10px; }
  .icon {
    width: 22px; height: 22px; border-radius: 50%;
    border: 1.5px solid var(--text-rose);
    display: flex; align-items: center; justify-content: center; flex: none;
  }
  .icon-plain { width: 16px; height: 16px; }
  .abn { position: absolute; right: 40px; top: 262px; font-size: 16px; letter-spacing: 0.5px; }
</style>
</head>
<body>
  <section class="card card-front">
    <div class="front-brand">
      <span class="brand-dot"></span>
      <span class="front-wordmark">QUELM</span>
    </div>
    <p class="front-web">www.quelm.com.au</p>
  </section>

  <section class="card card-back">
    <div class="back-brand">
      <span class="brand-dot"></span>
      <span class="back-wordmark">QUELM</span>
    </div>

    <div class="person">
      <p class="person-name">Suneha Parmeshwar</p>
      <p class="person-role">Founder</p>
    </div>

    <div class="rule"></div>

    <ul class="contact-list">
      <li>
        <span class="icon">
          <svg width="12" height="12" viewBox="0 0 24 24" fill="none" stroke="var(--text-rose)" stroke-width="2.4" stroke-linecap="round" stroke-linejoin="round"><path d="M22 16.9v3a2 2 0 0 1-2.2 2 19.8 19.8 0 0 1-8.6-3.1 19.5 19.5 0 0 1-6-6A19.8 19.8 0 0 1 2.1 4.2 2 2 0 0 1 4.1 2h3a2 2 0 0 1 2 1.7c.1.9.4 1.8.7 2.7a2 2 0 0 1-.5 2.1L8 9.8a16 16 0 0 0 6 6l1.3-1.3a2 2 0 0 1 2.1-.4c.9.3 1.8.6 2.7.7a2 2 0 0 1 1.7 2z"/></svg>
        </span>
        +61452190437
      </li>
      <li>
        <span class="icon">
          <svg width="12" height="12" viewBox="0 0 24 24" fill="none" stroke="var(--text-rose)" stroke-width="2.4" stroke-linejoin="round"><rect x="2" y="5" width="20" height="14" rx="2"/><path d="M2 7l10 7 10-7"/></svg>
        </span>
        suneha@quelm.com.au
      </li>
    </ul>

    <ul class="social-list">
      <li><span class="icon icon-plain"></span>quelm_jewellery</li>
      <li><span class="icon icon-plain"></span>@quelmjewellery</li>
    </ul>

    <p class="abn">ABN: 48291175034</p>
  </section>
</body>
</html>
```